Consulting firm looking for brochure design

Loring & Vance Consulting is a firm based in Fort Worth looking to update brochure design. We offer a broad range of development expertise to public, private and institutional clients. We would like to see brochure ideas including our company work, the services included, our individual qualifications and a list showing the clients we have served both public and private. We would like brochure to include the colors red, black, gray, and/or white only and to have our logo displayed on brochure pages. Files attached include a PPT with company information we'd like to see included in brochure, company logo designs to choose from to include in brochure, and the previous brochure that we are wanting to replace.
**Note that we are rebranding from " Warren Hollis Economic Development, LLC" to "Loring & Vance Consulting"**
**We have added a total of four logo designs; Two Portrait and Two Landscape both with the options of black backgrounds vs white backgrounds to choose from**

```html
<!DOCTYPE html>
<html lang="en">
<head>
<meta charset="utf-8">
<title>Loring &amp; Vance Consulting – Services Flyer</title>
<link href="https://fonts.googleapis.com/css2?family=Poppins:wght@400;500;600;700&family=Josefin+Sans:wght@400&display=swap" rel="stylesheet">
<style>
  :root {
    --backdrop: #959595;
    --paper: #f9f9f9;
    --red: #d3212d;
    --red-light: #e8333d;
    --charcoal: #505050;
    --ink: #2f2f2f;
    --white: #ffffff;
  }
  * { box-sizing: border-box; margin: 0; padding: 0; }
  html, body { width: 1200px; height: 1200px; overflow: hidden; background: var(--backdrop); }
  .canvas { position: relative; width: 1200px; height: 1200px; }
  .flyer {
    position: absolute; left: 261px; top: 117px; width: 688px; height: 974px;
    background: linear-gradient(160deg, #ffffff 0%, var(--paper) 60%, #f2f2f2 100%);
    overflow: hidden; font-family: "Poppins", sans-serif; color: var(--ink);
  }
  .top-band { position: absolute; left: 0; top: 0; width: 688px; height: 14px; }
  .brand {
    position: absolute; left: 0; top: 192px; width: 688px;
    display: flex; align-items: center; justify-content: center; gap: 16px;
    transform: translateY(-100%);
  }
  .brand-mark { width: 22px; height: 22px; background: var(--red); }
  .brand-name {
    font-family: "Josefin Sans", sans-serif; font-weight: 400; color: var(--ink);
    font-size: 28px; letter-spacing: 1.5px; line-height: 1.1; text-align: center;
  }
  .brand-name span { display: block; font-size: 18px; letter-spacing: 4px; }
  .headline {
    position: absolute; left: 0; top: 206px; width: 688px; text-align: center;
    font-weight: 700; font-size: 27px; color: var(--ink);
  }
  .intro {
    position: absolute; left: 72px; top: 252px; width: 556px; text-align: center;
    font-size: 16.8px; line-height: 19.4px; color: var(--ink);
  }
  .services-tab {
    position: absolute; left: 58px; top: 445px; width: 205px; height: 36px;
    background: var(--charcoal); border-top-right-radius: 34px;
    color: var(--white); font-weight: 500; font-size: 20px; padding: 3px 0 0 18px;
  }
  .services-panel {
    position: absolute; left: 58px; top: 480px; width: 288px; height: 422px;
    border-top-right-radius: 38px; border-bottom-left-radius: 38px;
    background: linear-gradient(118deg, var(--red) 0%, var(--red) 52%, var(--red-light) 64%, var(--red) 80%);
  }
  .service { position: absolute; left: 26px; display: flex; align-items: center; height: 56px; }
  .service svg { width: 56px; height: 56px; flex: none; }
  .service p { margin-left: 8px; color: var(--white); font-weight: 500; font-size: 14.6px; line-height: 16.2px; }
  .analysis { position: absolute; left: 379px; top: 476px; width: 290px; }
  .analysis h2 { font-weight: 700; font-size: 22px; line-height: 27px; color: var(--ink); }
  .analysis ul { list-style: none; margin-top: 12px; }
  .analysis li { position: relative; padding-left: 26px; font-size: 16.6px; line-height: 29px; }
  .analysis li svg { position: absolute; left: 2px; top: 9px; width: 18px; height: 13px; }
  .web-tab {
    position: absolute; left: 349px; top: 900px; width: 289px; height: 74px;
    background: var(--charcoal); border-top-right-radius: 40px;
    color: var(--white); font-weight: 600; font-size: 16px; letter-spacing: 2px;
    display: flex; align-items: center; justify-content: center; padding-right: 20px;
  }
</style>
</head>
<body>
<div class="canvas">
  <div class="flyer">
    <svg class="top-band" viewBox="0 0 688 14" aria-hidden="true">
      <polygon points="0,0 336,0 348,14 0,14" fill="var(--red)"/>
      <polygon points="348,0 688,0 688,14 360,14" fill="var(--charcoal)"/>
    </svg>

    <div class="brand">
      <div class="brand-mark"></div>
      <div class="brand-name">LORING &amp; VANCE<span>CONSULTING</span></div>
    </div>

    <h1 class="headline">LORING &amp; VANCE CONSULTING</h1>
    <p class="intro">Loring &amp; Vance Consulting offers a broad range of development expertise to public, private and institutional clients. With strategic guidance, we help navigate public-private partnerships, local government policies, creative incentive financing, project/program management, and many more of the challenges facing our clients. We present an unsurpassed level of quality and commitment by providing sensible solutions that are customized to meet the shifting needs of today’s economy.</p>

    <div class="services-tab">Services Include</div>
    <div class="services-panel">
      <div class="service" style="top:16px">
        <svg viewBox="0 0 56 56" aria-hidden="true"><polygon points="28,1 49,11 55,33 40,52 16,52 1,33 7,11" fill="none" stroke="#fff" stroke-width="1.3"/><path d="M16 30 l8 -6 l6 3 l10 -5 M18 32 l6 5 l10 -4" fill="none" stroke="#fff" stroke-width="1.4"/></svg>
        <p>Public Private<br>Partnership Structuring</p>
      </div>
      <div class="service" style="top:78px">
        <svg viewBox="0 0 56 56" aria-hidden="true"><polygon points="28,1 49,11 55,33 40,52 16,52 1,33 7,11" fill="none" stroke="#fff" stroke-width="1.3"/><path d="M17 38 v-5 M23 38 v-7 M29 38 v-9 M35 38 v-12 M16 27 l20 -9 m-4 0 h4 v4" fill="none" stroke="#fff" stroke-width="1.5"/></svg>
        <p>Incentive<br>Negotiations</p>
      </div>
      <div class="service" style="top:140px">
        <svg viewBox="0 0 56 56" aria-hidden="true"><polygon points="28,1 49,11 55,33 40,52 16,52 1,33 7,11" fill="none" stroke="#fff" stroke-width="1.3"/><rect x="19" y="15" width="18" height="25" fill="none" stroke="#fff" stroke-width="1.4"/><path d="M23 22 h10 M23 27 h10 M23 32 h7" stroke="#fff" stroke-width="1.3"/></svg>
        <p>Creating and<br>Amending Tax Increment<br>Reinvestments Zones</p>
      </div>
      <div class="service" style="top:203px">
        <svg viewBox="0 0 56 56" aria-hidden="true"><polygon points="28,1 49,11 55,33 40,52 16,52 1,33 7,11" fill="none" stroke="#fff" stroke-width="1.3"/><rect x="18" y="15" width="20" height="25" fill="none" stroke="#fff" stroke-width="1.4"/><path d="M22 30 l3 3 l6 -7" fill="none" stroke="#fff" stroke-width="1.5"/></svg>
        <p>Chapter 380 Grant<br>Contract Negotiations</p>
      </div>
      <div class="service" style="top:264px">
        <svg viewBox="0 0 56 56" aria-hidden="true"><polygon points="28,1 49,11 55,33 40,52 16,52 1,33 7,11" fill="none" stroke="#fff" stroke-width="1.3"/><path d="M16 40 v-14 l12 -8 l12 8 v14 z M25 40 v-8 h6 v8" fill="none" stroke="#fff" stroke-width="1.4"/></svg>
        <p>City Council<br>Workshops</p>
      </div>
      <div class="service" style="top:325px">
        <svg viewBox="0 0 56 56" aria-hidden="true"><polygon points="28,1 49,11 55,33 40,52 16,52 1,33 7,11" fill="none" stroke="#fff" stroke-width="1.3"/><rect x="16" y="17" width="24" height="18" fill="none" stroke="#fff" stroke-width="1.4"/><path d="M21 31 v-4 M26 31 v-7 M31 31 v-5 M36 31 v-9 M24 40 h8" stroke="#fff" stroke-width="1.4"/></svg>
        <p>Economic Impact<br>Reporting</p>
      </div>
    </div>

    <div class="analysis">
      <h2>Real Estate Financial<br>Analysis including</h2>
      <ul>
        <li><svg viewBox="0 0 18 13" aria-hidden="true"><path d="M1 1 l6 5.5 l-6 5.5 M8 1 l6 5.5 l-6 5.5" fill="none" stroke="var(--red)" stroke-width="2.6"/></svg>Taxable Value Analysis</li>
        <li><svg viewBox="0 0 18 13" aria-hidden="true"><path d="M1 1 l6 5.5 l-6 5.5 M8 1 l6 5.5 l-6 5.5" fill="none" stroke="var(--red)" stroke-width="2.6"/></svg>Pro-forma Analysis</li>
        <li><svg viewBox="0 0 18 13" aria-hidden="true"><path d="M1 1 l6 5.5 l-6 5.5 M8 1 l6 5.5 l-6 5.5" fill="none" stroke="var(--red)" stroke-width="2.6"/></svg>Underwriting of Incentive<br>Package</li>
        <li><svg viewBox="0 0 18 13" aria-hidden="true"><path d="M1 1 l6 5.5 l-6 5.5 M8 1 l6 5.5 l-6 5.5" fill="none" stroke="var(--red)" stroke-width="2.6"/></svg>Market/Financial Feasibility</li>
        <li><svg viewBox="0 0 18 13" aria-hidden="true"><path d="M1 1 l6 5.5 l-6 5.5 M8 1 l6 5.5 l-6 5.5" fill="none" stroke="var(--red)" stroke-width="2.6"/></svg>Cost/Benefit Analysis</li>
        <li><svg viewBox="0 0 18 13" aria-hidden="true"><path d="M1 1 l6 5.5 l-6 5.5 M8 1 l6 5.5 l-6 5.5" fill="none" stroke="var(--red)" stroke-width="2.6"/></svg>Appraisal review</li>
      </ul>
    </div>

    <div class="web-tab">WWW.LVCG.COM</div>
  </div>
</div>
</body>
</html>
```